Letterhead Design Project

Looking for letterhead designs for Dravesco Mining.

I am looking for a letterhead design in conjunction with a business card design. I have opened contests for both but ask that if you submit a letterhead design you also submit a business card design with a corresponding look/feel.

Dravesco Mining is a B2B company that buys and sells large machinery tires within the coal mining industry. The design should the strong, crisp and masculine. I have uploaded the company logo and mock-up of the back of the company's business card.

Color scheme should be grey/green/black

Contact information to include:
Name: Tom Sealbrook
Title: Managing Director
Phone: 555-314-2097
Address: 1186 Pelham #3 Dallas, TX 75209
Email: Tom@Dravesco.example

Project Deadline Extended
Reason: Looking for a more refined, elegant letterhead than what's been submitted as of yet. Here is a sample of what we're looking for: http://www.plumbridgestudio.example/letterhead-designs/ We will also be increasing the payment.

```html
<!DOCTYPE html>
<html lang="en">
<head>
<meta charset="utf-8">
<title>Dravesco Mining — Letterhead</title>
<link href="https://fonts.googleapis.com/css2?family=Open+Sans:wght@400;700&family=Allura&display=swap" rel="stylesheet">
<style>
  :root {
    --backdrop: #d9d9d6;
    --paper: #ffffff;
    --ink: #1e1e1e;
    --ink-soft: #3a3a3a;
    --brand-green: #62b93f;
    --brand-black: #0d0d0d;
  }
  * { box-sizing: border-box; margin: 0; padding: 0; }
  html, body {
    width: 1200px; height: 1024px; overflow: hidden;
    background: var(--backdrop);
    font-family: "Open Sans", Arial, sans-serif;
    color: var(--ink);
  }
  .letterhead {
    position: absolute; left: 260px; top: 31px;
    width: 680px; height: 962px;
    background: var(--paper);
    box-shadow: 0 6px 24px rgba(0,0,0,.25);
  }
  .brand {
    position: absolute; left: 58px; top: 62px;
    display: flex; align-items: center; gap: 12px;
  }
  .brand-square { width: 22px; height: 22px; background: var(--brand-green); }
  .brand-name {
    font-weight: 700; font-size: 26px; letter-spacing: 1.5px;
    color: var(--brand-black); text-transform: uppercase;
  }
  .contact {
    position: absolute; right: 48px; top: 150px;
    font-style: normal;
    text-align: right; font-size: 11.5px; line-height: 17px; color: var(--ink-soft);
  }
  .contact-line { display: flex; justify-content: flex-end; align-items: center; gap: 6px; }
  .contact-line svg { width: 10px; height: 10px; fill: var(--brand-green); flex: 0 0 10px; }
  .letter {
    position: absolute; left: 58px; top: 215px; width: 560px;
  }
  .salutation { font-size: 14px; line-height: 18px; color: var(--ink); margin-bottom: 12px; }
  .letter-body { font-size: 11.5px; line-height: 15.5px; color: var(--ink-soft); }
  .letter-body p { margin-left: 44px; margin-bottom: 12px; }
  .sign-off { margin-top: 26px; }
  .signature { font-family: "Allura", cursive; font-size: 28px; color: var(--ink-soft); line-height: 1; }
  .sign-title { font-size: 11px; color: var(--ink-soft); margin-top: 4px; }
  .footer-band {
    position: absolute; left: 0; bottom: 0; width: 100%; height: 30px; display: flex;
  }
  .footer-band .band-green { flex: 0 0 71%; background: var(--brand-green); }
  .footer-band .band-black { flex: 1; background: var(--brand-black); }
</style>
</head>
<body>
  <main class="letterhead">
    <header class="brand">
      <span class="brand-square"></span>
      <span class="brand-name">Dravesco Mining</span>
    </header>

    <address class="contact">
      <div class="contact-line">555-314-2097
        <svg viewBox="0 0 10 10"><path d="M2 0.5l2 2-1 1.3c.6 1.3 1.8 2.5 3.2 3.2l1.3-1 2 2-1.3 1.5C4.5 9.5.5 5.5.5 1.8z"/></svg>
      </div>
      <div class="contact-line">Tom@Dravesco.example
        <svg viewBox="0 0 10 10"><path d="M0 2h10v6H0zM0 2l5 3.5L10 2"/></svg>
      </div>
      <div class="contact-line">1186 Pelham #3 Dallas, TX 75209
        <svg viewBox="0 0 10 10"><path d="M5 0a3.5 3.5 0 0 0-3.5 3.5C1.5 6 5 10 5 10s3.5-4 3.5-6.5A3.5 3.5 0 0 0 5 0zm0 5a1.5 1.5 0 1 1 0-3 1.5 1.5 0 0 1 0 3z"/></svg>
      </div>
    </address>

    <article class="letter">
      <p class="salutation">Lorem Ipsum,</p>
      <section class="letter-body">
        <p>Duis sit amet dolor sit amet dolor tempor iaculis ac nec ante. Proin nunc diam, egestas eu semper a, fermentum ac leo. Fusce sit amet tempor elit. Mauris auctor interdum massa vitae cursus. Ut adipiscing pellentesque nunc, eget tincidunt magna imperdiet non. Curabitur eleifend elementum nisl eget iaculis. Suspendisse scelerisque ligula a nunc faucibus sit amet elementum dolor dictum.</p>
        <p>Praesent condimentum mi at ultrices fermentum. Ipsum lectus consequat mauris, ut vulputate nibh erat id eros. Vivamus ornare mattis libero at dictum. Praesent sodales metus sed nulla laoreet mollis. Curabitur non turpis in orci dignissim gravida. Aliquam tristique mauris a nibh vestibulum sagittis.</p>
        <p>Duis porta semper nibh, tincidunt aliquam metus euismod eget. Morbi varius varius pellentesque. Donec aliquam vulputate tortor non hendrerit. Suspendisse at ipsum ante, interdum porttitor ligula. Curabitur eu molestie sapien. Sed magna purus, faucibus quis pulvinar nec, commodo vel justo. Nam faucibus ornare varius. Vivamus sit amet felis vitae justo scelerisque malesuada. Etiam venenatis vehicula magna, a eleifend lorem ornare nec. Maecenas eu nisl vel nunc aliquet malesuada vel in lacus.</p>
        <p>Morbi et odio eu ante pharetra iaculis vitae eget arcu. Maecenas gravida, dui vel ultricies aliquet, dui arcu luctus ante, non dignissim ipsum tortor vel orci, um fringilla mi. Mauris porta feugiat nibh et fermentum. Donec scelerisque consequat lacinia.</p>
        <p>Curabitur ac diam at quam ultrices laoreet at ut tellus. Maecenas vitae urna in lorem condimentum sollicitudin eget vel lacus. Ut nisi turpis, tristique ullamcorper laoreet nec, gravida nec est. Donec elementum malesuada volutpat. In ac arcu quis augue vehicula fringilla.</p>
      </section>
      <footer class="sign-off">
        <div class="signature">Yours Name</div>
        <div class="sign-title">Company Director</div>
      </footer>
    </article>

    <div class="footer-band"><span class="band-green"></span><span class="band-black"></span></div>
  </main>
</body>
</html>
```